Create a Valdossi-looking dashboard for our Quiet Harbor Speedometer that can look similar to my AI-generated dashboard attached, but with: 1) clear borders on all four sides, 2) is created in a way that we can modify the numbers weekly, say maybe you create the graphic that we can inset the excel spreadsheet numbers into, but ideally mixed with the Valdossi look black leather bubble design shown in the dashboard?; 3) uses the exact numbers shown in the attachment; 4) the speedometer on top should have four equal colors of red on left (-1), then yellow (0), then light green (1), then medium green (2); 5) the gauge on the top left should be the graphic that includes 0-100% bar that is currently 33%, and right below that a -20 to +20 bar with the arrow pointing to 11.9%, with color coding similar to the graphic; 6) replace the Valdossi logo in the middle with a similar shaped shield with blue background with the "T" logo with the eagle inside it, like attached

```html
<!DOCTYPE html>
<html lang="en">
<head>
<meta charset="utf-8">
<title>Quiet Harbor Speedometer</title>
<link rel="stylesheet" href="https://fonts.googleapis.com/css2?family=Cinzel:wght@800;900&family=Open+Sans:wght@600;700&family=Roboto:wght@700;900&family=Libre+Baskerville:wght@700&display=swap">
<style>
  :root{
    --cabin-top:#3a3c41;
    --cabin-bottom:#1a1b1e;
    --leather-light:#3b3b3e;
    --leather-dark:#0e0e10;
    --bezel:#1a1b1f;
    --bezel-edge:#55585e;
    --silver:#d9dde2;
    --dial-blue:#16304a;
    --dial-blue-deep:#0b1826;
    --navy:#0a2a66;
    --navy-bright:#0d43b4;
    --band-red:#d81e16;
    --band-yellow:#f2de1e;
    --band-light-green:#8fd84a;
    --band-medium-green:#1f9a3a;
    --gear-turbo:#45d15a;
    --gear-accel:#8fe38f;
    --gear-brakes:#ffff00;
    --gear-reverse:#ff0a0a;
    --reverse-text:#8a0000;
    --trend-grey:#c9c9c9;
    --trend-grey-light:#eeeeee;
    --gold:#e3a93a;
    --yellow-value:#f6e23a;
    --white:#ffffff;
    --ink:#111111;
    --led:#ff2a2a;
  }
  *{box-sizing:border-box;margin:0;padding:0}
  html,body{width:1200px;height:820px;overflow:hidden;background:#0c0c0c}
  .dashboard{position:relative;width:1200px;height:820px;
    background:linear-gradient(90deg,#1b1b1b 0%,#777 20%,#1c1c1c 45%,#777 70%,#1b1b1b 100%);}
  .backdrop{position:absolute;left:29px;top:29px;width:1141px;height:760px}
  .center-gauge,.side-gauge,.title,.data-panel,.lower-panel,.date-range,.start-button{position:absolute}
  .center-gauge{left:398px;top:80px;width:420px;height:220px}
  .side-gauge{top:192px;width:210px;height:190px}
  .side-gauge.completion{left:170px}
  .side-gauge.change{left:826px}
  .gauge-text{position:absolute;width:100%;text-align:center;font-family:"Roboto",sans-serif;font-weight:900;color:var(--white)}
  .completion .pct{top:66px;font-size:40px;text-shadow:0 2px 3px #000}
  .completion .ratio{top:112px;font-size:17px;font-weight:700;letter-spacing:1px;color:#e6e9ee}
  .change .pct{top:70px;left:-4px;font-size:40px;color:var(--yellow-value);text-shadow:0 2px 3px #000}
  .brand{position:absolute;left:560px;top:150px;width:96px;display:flex;align-items:center;justify-content:center;gap:5px;
    font-family:"Open Sans",sans-serif;font-weight:700;font-size:10px;color:var(--white);white-space:nowrap;text-shadow:0 1px 2px #000}
  .brand-dot{width:10px;height:10px;border-radius:50%;background:var(--navy-bright)}
  .title{left:0;width:1212px;top:308px;text-align:center;font-family:"Cinzel",serif;font-weight:900;font-size:25px;letter-spacing:.5px;
    color:var(--gold);text-shadow:0 2px 2px #000}
  .data-panel{left:250px;top:346px;width:706px;height:230px;border-radius:22px;border:4px solid var(--silver);
    background:linear-gradient(180deg,#0d1d2e 0%,#1f3f5e 55%,#0d1d2e 100%);box-shadow:0 0 0 3px #333,0 4px 10px #000}
  .lower-panel{left:301px;top:610px;width:596px;height:171px;border-radius:18px 18px 6px 6px;
    background:linear-gradient(180deg,#12243a 0%,#1a3553 50%,#0c1a29 100%);border:2px solid #3a3f46}
  table{border-collapse:collapse;font-family:"Open Sans",sans-serif;font-weight:700;font-size:10.5px;color:var(--ink);position:absolute}
  .trend-table{left:13px;top:34px;width:674px}
  .history-table{left:42px;top:13px;width:510px}
  td,th{height:15.4px;line-height:14px;border:1px solid #555;padding:0;text-align:center;white-space:nowrap}
  th{background:var(--navy);color:var(--white);text-decoration:underline;font-weight:700}
  th.col-trend{background:linear-gradient(90deg,var(--navy),var(--navy-bright),var(--navy))}
  .col-gear{width:210px}
  .col-trend{width:300px}
  .col-change{width:164px}
  td.gear{text-align:left}
  td.gear .num{display:inline-block;width:66px;text-align:right;margin-right:7px}
  .turbo td.gear{background:var(--gear-turbo)}
  .accel td.gear{background:var(--gear-accel)}
  .brakes td.gear{background:var(--gear-brakes)}
  .reverse td.gear{background:var(--gear-reverse);color:var(--reverse-text)}
  td.trend,td.change{background:linear-gradient(90deg,var(--trend-grey),var(--trend-grey-light) 60%,var(--trend-grey))}
  .turbo td.trend{background:linear-gradient(90deg,var(--gear-turbo),#7df09a 50%,var(--gear-turbo))}
  .turbo td.change{background:var(--gear-turbo)}
  .date-range{left:747px;top:587px;font-family:"Libre Baskerville",serif;font-weight:700;font-size:13px;color:#e8e8e8;text-shadow:0 1px 2px #000}
  .start-button{left:141px;top:527px;width:70px;height:70px;border-radius:50%;
    background:radial-gradient(circle at 50% 40%,#d3242b,#7a0a0e 75%);border:3px solid #bfc3c8;box-shadow:0 0 0 3px #222,0 3px 8px #000;
    display:flex;flex-direction:column;align-items:center;justify-content:center;font-family:"Roboto",sans-serif;font-weight:700;color:#f3f3f3;line-height:1.1}
  .start-button .line{font-size:10px}
  .start-button .small{font-size:7px;margin-top:2px}
</style>
</head>
<body>
<main class="dashboard">

  <svg class="backdrop" viewBox="0 0 1141 760" role="img" aria-label="Black stitched leather car dashboard backdrop">
    <defs>
      <linearGradient id="leather" x1="0" y1="0" x2="0" y2="1">
        <stop offset="0" stop-color="#3b3b3e"/><stop offset=".5" stop-color="#1e1e21"/><stop offset="1" stop-color="#0e0e10"/>
      </linearGradient>
      <linearGradient id="cabin" x1="0" y1="0" x2="0" y2="1">
        <stop offset="0" stop-color="#3a3c41"/><stop offset="1" stop-color="#1a1b1e"/>
      </linearGradient>
    </defs>
    <rect width="1141" height="760" fill="url(#cabin)"/>
    <path d="M0,170 C120,130 260,110 370,78 Q579,-5 788,78 C900,110 1040,130 1141,150 L1141,360 C1060,330 990,300 930,300 L250,300 C170,300 90,330 0,360 Z" fill="url(#leather)" stroke="#4a4a4e" stroke-width="2"/>
    <path d="M0,180 C120,140 260,120 372,88 Q579,5 786,88 C900,120 1040,140 1141,160" fill="none" stroke="#5a5a5f" stroke-width="1.5" stroke-dasharray="5 4"/>
    <path d="M0,350 C80,330 160,330 220,360 L230,760 L0,760 Z" fill="url(#leather)" stroke="#4a4a4e" stroke-width="2"/>
    <path d="M1141,350 C1060,330 980,330 930,360 L930,760 L1141,760 Z" fill="url(#leather)" stroke="#4a4a4e" stroke-width="2"/>
    <ellipse cx="245" cy="268" rx="135" ry="125" fill="#1a1b1f" stroke="#55585e" stroke-width="3"/>
    <ellipse cx="903" cy="268" rx="135" ry="125" fill="#1a1b1f" stroke="#55585e" stroke-width="3"/>
    <path d="M360,270 Q579,-10 798,270 Z" fill="#1a1b1f" stroke="#55585e" stroke-width="3"/>
    <rect x="200" y="270" width="741" height="60" fill="#1e1f23"/>
    <circle cx="20" cy="250" r="48" fill="#111" stroke="#666" stroke-width="4"/>
    <circle cx="1150" cy="270" r="48" fill="#111" stroke="#666" stroke-width="4"/>
    <circle cx="335" cy="158" r="5" fill="#ff2a2a"/>
    <circle cx="816" cy="158" r="5" fill="#ff2a2a"/>
  </svg>

  <svg class="center-gauge" viewBox="0 0 420 220" aria-label="Gear gauge from -1 to 2, needle in gear 1">
    <defs>
      <radialGradient id="bowlShade" cx=".5" cy="1" r=".6">
        <stop offset=".3" stop-color="#000" stop-opacity=".3"/><stop offset="1" stop-color="#000" stop-opacity="0"/>
      </radialGradient>
      <linearGradient id="needleGold" x1="0" y1="0" x2="1" y2="0">
        <stop offset="0" stop-color="#b9801e"/><stop offset=".5" stop-color="#ffe07a"/><stop offset="1" stop-color="#c98a22"/>
      </linearGradient>
    </defs>
    <path d="M7,208 A203,203 0 0 1 413,208" fill="none" stroke="#cfd3d8" stroke-width="6"/>
    <path class="band-reverse" d="M210,208 L15,208 A195,195 0 0 1 72.1,70.1 Z" fill="var(--band-red)"/>
    <path class="band-brakes" d="M210,208 L72.1,70.1 A195,195 0 0 1 210,13 Z" fill="var(--band-yellow)"/>
    <path class="band-accelerator" d="M210,208 L210,13 A195,195 0 0 1 347.9,70.1 Z" fill="var(--band-light-green)"/>
    <path class="band-turbo" d="M210,208 L347.9,70.1 A195,195 0 0 1 405,208 Z" fill="var(--band-medium-green)"/>
    <path d="M15,208 A195,195 0 0 1 405,208 Z" fill="url(#bowlShade)"/>
    <g stroke="#fff" stroke-linecap="round">
      <line x1="210" y1="25" x2="210" y2="45" stroke-width="3" transform="rotate(-90 210 208)"/>
      <line x1="210" y1="25" x2="210" y2="38" stroke-width="2" transform="rotate(-80 210 208)"/>
      <line x1="210" y1="25" x2="210" y2="38" stroke-width="2" transform="rotate(-70 210 208)"/>
      <line x1="210" y1="25" x2="210" y2="45" stroke-width="3" transform="rotate(-60 210 208)"/>
      <line x1="210" y1="25" x2="210" y2="38" stroke-width="2" transform="rotate(-50 210 208)"/>
      <line x1="210" y1="25" x2="210" y2="38" stroke-width="2" transform="rotate(-40 210 208)"/>
      <line x1="210" y1="25" x2="210" y2="45" stroke-width="3" transform="rotate(-30 210 208)"/>
      <line x1="210" y1="25" x2="210" y2="38" stroke-width="2" transform="rotate(-20 210 208)"/>
      <line x1="210" y1="25" x2="210" y2="38" stroke-width="2" transform="rotate(-10 210 208)"/>
      <line x1="210" y1="25" x2="210" y2="45" stroke-width="3"/>
      <line x1="210" y1="25" x2="210" y2="38" stroke-width="2" transform="rotate(10 210 208)"/>
      <line x1="210" y1="25" x2="210" y2="38" stroke-width="2" transform="rotate(20 210 208)"/>
      <line x1="210" y1="25" x2="210" y2="45" stroke-width="3" transform="rotate(30 210 208)"/>
      <line x1="210" y1="25" x2="210" y2="38" stroke-width="2" transform="rotate(40 210 208)"/>
      <line x1="210" y1="25" x2="210" y2="38" stroke-width="2" transform="rotate(50 210 208)"/>
      <line x1="210" y1="25" x2="210" y2="45" stroke-width="3" transform="rotate(60 210 208)"/>
      <line x1="210" y1="25" x2="210" y2="38" stroke-width="2" transform="rotate(70 210 208)"/>
      <line x1="210" y1="25" x2="210" y2="38" stroke-width="2" transform="rotate(80 210 208)"/>
      <line x1="210" y1="25" x2="210" y2="45" stroke-width="3" transform="rotate(90 210 208)"/>
    </g>
    <g font-family="Roboto, sans-serif" font-weight="900" font-size="38" fill="#fff" stroke="#333" stroke-width="1" text-anchor="middle">
      <text x="130" y="98">0</text>
      <text x="279" y="93">1</text>
      <text x="62" y="200">-1</text>
      <text x="356" y="200">2</text>
    </g>
    <path d="M138,208 A72,72 0 0 1 282,208" fill="none" stroke="#d6d9de" stroke-width="8"/>
    <polygon points="204,182 216,192 297,105" fill="url(#needleGold)"/>
    <circle cx="210" cy="187" r="14" fill="url(#needleGold)" stroke="#8a5d12" stroke-width="1.5"/>
  </svg>

  <div class="brand"><span class="brand-dot"></span>Quiet Harbor</div>

  <div class="side-gauge completion">
    <svg width="210" height="190" viewBox="0 0 210 190" aria-label="Completion gauge at 33 percent">
      <circle cx="105" cy="110" r="98" fill="var(--dial-blue)" stroke="#9aa0a8" stroke-width="4"/>
      <circle cx="105" cy="110" r="70" fill="var(--dial-blue-deep)" opacity=".5"/>
      <path d="M24,152 A90,90 0 1 1 192,86" fill="none" stroke="#d3d7dc" stroke-width="14"/>
      <path d="M24,152 A90,90 0 0 1 38,50" fill="none" stroke="#3f63c2" stroke-width="14"/>
      <line x1="34" y1="43" x2="44" y2="56" stroke="#f2b233" stroke-width="3"/>
      <g font-family="Roboto, sans-serif" font-weight="700" font-size="8" fill="#cfd6de" text-anchor="middle">
        <text x="38" y="142">0</text>
        <text x="38" y="100">20</text>
        <text x="57" y="66">40</text>
        <text x="93" y="46">60</text>
        <text x="134" y="54">80</text>
        <text x="164" y="88">100</text>
      </g>
    </svg>
    <div class="gauge-text pct">33%</div>
    <div class="gauge-text ratio">(162/500)</div>
  </div>

  <div class="side-gauge change">
    <svg width="210" height="190" viewBox="0 0 210 190" aria-label="Change gauge from -20 to 20, pointer at 11.9 percent">
      <defs>
        <linearGradient id="heat" x1="0" y1="0" x2="0" y2="1">
          <stop offset="0" stop-color="#fff8b0"/><stop offset=".5" stop-color="#f2c21a"/><stop offset="1" stop-color="#d0201a"/>
        </linearGradient>
      </defs>
      <circle cx="105" cy="110" r="98" fill="var(--dial-blue)" stroke="#9aa0a8" stroke-width="4"/>
      <path d="M18,140 A90,90 0 0 1 90,21" fill="none" stroke="#22a83a" stroke-width="12"/>
      <path d="M90,21 A90,90 0 0 1 182,64" fill="none" stroke="#e9ecef" stroke-width="12"/>
      <path d="M182,64 A90,90 0 0 1 170,172" fill="none" stroke="url(#heat)" stroke-width="14"/>
      <line x1="193" y1="64" x2="170" y2="76" stroke="#f2b233" stroke-width="4"/>
      <g font-family="Roboto, sans-serif" font-weight="700" font-size="8" fill="#cfd6de" text-anchor="middle">
        <text x="36" y="130">-20</text>
        <text x="55" y="60">-10</text>
        <text x="108" y="38">0</text>
        <text x="162" y="70">10</text>
        <text x="165" y="152">20</text>
      </g>
    </svg>
    <div class="gauge-text pct">11,9%</div>
  </div>

  <h1 class="title">QUIET HARBOR SPEEDOMETER</h1>

  <section class="data-panel">
    <table class="trend-table">
      <tr><th class="col-gear">GEAR</th><th class="col-trend">CURRENT TREND</th><th class="col-change">LAST TREND CHANGE</th></tr>
      <tr class="turbo"><td class="gear"><span class="num">2</span>TURBO BOOST</td><td class="trend">BULL</td><td class="change">Friday, August 15, 2025</td></tr>
      <tr class="accel"><td class="gear"><span class="num">1</span>ACCELERATOR PEDAL</td><td class="trend">BULLISH</td><td class="change"></td></tr>
      <tr class="brakes"><td class="gear"><span class="num">0</span>BRAKES</td><td class="trend">BEARISH</td><td class="change"></td></tr>
      <tr class="reverse"><td class="gear"><span class="num">-1</span>REVERSE</td><td class="trend">BEAR</td><td class="change"></td></tr>
      <tr><th class="col-gear">GEAR</th><th class="col-trend">CURRENT TREND</th><th class="col-change">LAST TREND CHANGE</th></tr>
      <tr class="turbo"><td class="gear"><span class="num">2</span>TURBO BOOST</td><td class="trend">BULL</td><td class="change">Friday, August 15, 2025</td></tr>
      <tr class="accel"><td class="gear"><span class="num">1</span>ACCELERATOR PEDAL</td><td class="trend">BULLISH</td><td class="change"></td></tr>
      <tr class="brakes"><td class="gear"><span class="num">0</span>BRAKES</td><td class="trend">BEARISH</td><td class="change"></td></tr>
      <tr class="reverse"><td class="gear"><span class="num">-1</span>REVERSE</td><td class="trend">BEAR</td><td class="change"></td></tr>
    </table>
  </section>

  <p class="date-range">07/05/2005 TO 13/01/2024</p>

  <div class="start-button"><span class="line">ENGINE</span><span class="line">START</span><span class="small">6:13</span></div>

  <section class="lower-panel">
    <table class="history-table">
      <tr><th class="col-gear">GEAR</th><th class="col-trend">CURRENT TREND</th></tr>
      <tr class="turbo"><td class="gear"><span class="num">2</span>TURBO BOOST</td><td class="trend">BULL</td></tr>
      <tr class="accel"><td class="gear"><span class="num">1</span>ACCELERATOR PEDAL</td><td class="trend">BULLISH</td></tr>
      <tr class="brakes"><td class="gear"><span class="num">0</span>BRAKES</td><td class="trend">BEARISH</td></tr>
      <tr class="reverse"><td class="gear"><span class="num">-1</span>REVERSE</td><td class="trend">BEAR</td></tr>
      <tr class="turbo"><td class="gear"><span class="num">2</span>TURBO BOOST</td><td class="trend">BULL</td></tr>
      <tr class="accel"><td class="gear"><span class="num">1</span>ACCELERATOR PEDAL</td><td class="trend">BULLISH</td></tr>
      <tr class="brakes"><td class="gear"><span class="num">0</span>BRAKES</td><td class="trend">BEARISH</td></tr>
      <tr class="reverse"><td class="gear"><span class="num">-1</span>REVERSE</td><td class="trend">BEAR</td></tr>
    </table>
  </section>

</main>
</body>
</html>
```